Website refresh

We are a leading provide of JTAG hardware and software tools. We provide affordable USB and Ethernet solutions that are easily integrated into applications via a common API for Windows and Linux platforms. Our product simplicity, integration with third party applications, and free utilities have made us the provider of choice for Summit200 companies, small businesses as well as academic and research institutions.

JTAG is an industry standard interface by which hardware and software engineers can debug, test and program their hardware or software.

Target Market(s)

We are in the technology industry, and our target audience includes hardware engineers, low level embedded software engineers, and ASIC designers.

Industry/Entity Type

Software

Requirements
Must have
• The artwork for the slider must incorporate the product photos provided.

Our new website will be a facelift for our current website (www.pelvora-kits.com), and must allow all the content on the current website to be incorporate into the new website (the new website may have a new CMS).
Nice to have
• Please use the screen sketches as guidance. It does not have to follow this exactly, but should allow for the various elements to be incorporated.

The design I liked is by Tobias Grennholt - his Meadow template.
http://tobiasgrennholt.com/templates/meadow/

here is the live demo:
http://tobiasgrennholt.com/files/demo/meadow/

What do you think about this? Would welcome your opinion. My product is in black plastic:
http://www.pelvora-kits.com/index.php?main_page=quenmar

so I hope that some picture of this (to replace the photos in the templates) will work well. (I will need to include landing
pages like the one above into the new site, and there will be a few like this for other potential customers)

I would be also nice to exchange some ideas on the scrolling/rolling logos for customers (company logos) an partners (company logos)

Please let me know your thoughts.

If you are also able to do web programming, or work with someone who might be able to assist with web programming and migrating the website (while incorporating the new template), then please let me know separately.

```html
<!DOCTYPE html>
<html lang="en">
<head>
<meta charset="utf-8">
<title>PelvoraKits – JTAG cables and tools</title>
<link rel="stylesheet" href="https://fonts.googleapis.com/css2?family=Ubuntu:wght@400;500;700&family=Open+Sans:wght@400;600;700&display=swap">
<style>
:root{
  --purple:#7a3f8e;
  --ink:#1b1b1b;
  --text:#333;
  --muted:#6f6f6f;
  --rule:#e6e6e6;
  --line:#ececec;
  --mark:#2a2a2a;
  --white:#fff;
}
*{margin:0;padding:0;box-sizing:border-box}
html,body{width:1200px;height:996px;overflow:hidden;background:var(--white)}
body{position:relative;font-family:"Open Sans",Arial,sans-serif;color:var(--text)}
.abs{position:absolute}

/* header */
.site-header{position:absolute;left:0;top:0;width:1200px;height:143px;
  background:linear-gradient(#fafafa,#fff 60%,#f3f3f3);border-top:4px solid #dcdcdc}
.brand{left:48px;top:46px;font-family:"Ubuntu",sans-serif;font-size:33px;font-weight:500;color:var(--ink);letter-spacing:-.5px}
.brand span{color:var(--purple)}
.tagline{left:48px;top:86px;font-size:13px;font-weight:700;color:var(--ink)}
.main-nav a{position:absolute;top:80px;font-family:"Ubuntu",sans-serif;font-size:19px;color:#555;text-decoration:none;transform:translateX(-50%)}
.nav-sep{position:absolute;top:58px;width:1px;height:62px;background:#e2e2e2}
.cart{left:1027px;top:81px;display:flex;align-items:center;gap:8px;font-size:13px;color:#666}

/* hero */
.hero{position:absolute;left:0;top:143px;width:1200px;height:377px;
  background:linear-gradient(#fff,#fafafa 55%,#eeeeee);border-bottom:1px solid #ddd;box-shadow:0 2px 4px rgba(0,0,0,.06)}
.product-shot{left:103px;top:74px;width:354px;height:252px;border-radius:18px;
  background:linear-gradient(160deg,#5a5e60,#3c3f41 55%,#2b2d2f);box-shadow:0 12px 14px -8px rgba(0,0,0,.35)}
.hero-title{left:486px;top:84px;font-family:"Ubuntu",sans-serif;font-size:25px;color:var(--purple)}
.hero-sub{left:486px;top:121px;font-family:"Ubuntu",sans-serif;font-size:17px;color:var(--ink)}
.hero-copy{left:486px;top:153px;width:648px;font-size:13px;line-height:21px;color:var(--muted);text-align:justify}
.hero-copy p+p{margin-top:4px}
.btn-more{left:486px;top:266px;width:109px;height:27px;border-radius:3px;background:var(--purple);color:#fff;
  font-family:"Ubuntu",sans-serif;font-size:14px;line-height:27px;text-align:center}
.slider-dots{left:1058px;top:331px;display:flex;gap:11px}
.slider-dots i{width:19px;height:19px;border-radius:50%;background:#000}
.slider-dots i.active{background:var(--purple)}

/* columns */
.col-title{position:absolute;top:566px;font-family:"Ubuntu",sans-serif;font-size:22px;color:var(--ink)}
.col-rule{position:absolute;top:600px;height:4px;background:var(--rule)}
.col-sep{position:absolute;top:555px;width:1px;height:290px;background:var(--line)}
.view-all{left:306px;top:573px;font-size:14px;color:var(--ink)}
.news-item{position:absolute;left:41px;width:327px}
.news-item h3{font-size:15px;font-weight:400;color:var(--ink);margin-bottom:2px}
.news-item p{font-size:13px;line-height:21px;color:var(--muted);text-align:justify}

.partner{position:absolute;font-family:"Ubuntu",sans-serif;font-weight:700;font-size:28px;color:var(--mark)}

.client{position:absolute;width:102px;height:79px;border:1px solid #e2e2e2;border-radius:5px;background:#fff;
  box-shadow:0 1px 3px rgba(0,0,0,.08);display:flex;align-items:center;justify-content:center;
  font-family:"Ubuntu",sans-serif;font-weight:700;font-size:19px;color:var(--mark)}

/* footer */
.site-footer{position:absolute;left:0;top:877px;width:1200px;height:119px;background:linear-gradient(#efefef,#f7f7f7 30%,#f7f7f7);border-top:1px solid #e4e4e4}
.footer-nav{position:absolute;top:27px;width:1200px;text-align:center;font-size:13px;color:#444}
.footer-nav span{margin:0 7px;color:#666}
.copyright{position:absolute;top:64px;width:1200px;text-align:center;font-size:12px;color:#555}
</style>
</head>
<body>

<header class="site-header">
  <div class="abs brand">Pelvora<span>Kits</span></div>
  <div class="abs tagline">JTAG cables and tools for developers and engineers</div>
  <nav class="main-nav">
    <a style="left:525px">Product</a>
    <span class="nav-sep" style="left:592px"></span>
    <a style="left:671px">Download</a>
    <span class="nav-sep" style="left:751px"></span>
    <a style="left:816px">Support</a>
    <span class="nav-sep" style="left:881px"></span>
    <a style="left:939px">Login</a>
    <span class="nav-sep" style="left:1000px"></span>
  </nav>
  <div class="abs cart">
    <svg width="26" height="22" viewBox="0 0 26 22" fill="none" stroke="#555" stroke-width="2" stroke-linejoin="round">
      <path d="M1 2h4l3 12h13l3-9H7"/><circle cx="10" cy="19" r="1.8" fill="#555"/><circle cx="19" cy="19" r="1.8" fill="#555"/>
    </svg>
    <span>(2) items - $24.00</span>
  </div>
</header>

<section class="hero">
  <div class="abs product-shot" role="img" aria-label="Photo of the black plastic JTAG cable unit with error and ready status lights"></div>
  <h1 class="abs hero-title" style="font-weight:400">Product Punch line &amp; Review</h1>
  <h2 class="abs hero-sub" style="font-weight:400">tittle line goes here</h2>
  <div class="abs hero-copy">
    <p>Brightmoor eSolutions is a web service company, offering a wide range of services which range from designing and development, that is covering.</p>
    <p>To be the best we know what and how to present beautifully the working of the client’s need and their advantages be highlighted.</p>
  </div>
  <div class="abs btn-more">learn more</div>
  <div class="abs slider-dots"><i class="active"></i><i></i><i></i><i></i></div>
</section>

<section>
  <h2 class="col-title" style="left:40px;font-weight:400">Latest News</h2>
  <div class="abs view-all">View all</div>
  <div class="col-rule" style="left:37px;width:342px"></div>
  <article class="news-item" style="top:621px">
    <h3>Product Name here</h3>
    <p>To be the best we know what and how to present beautifully the working of the client’s need and their advantages be highlighted. We act in accordance with the Industry certified processes.</p>
  </article>
  <article class="news-item" style="top:744px">
    <h3>Product Name here</h3>
    <p>To be the best we know what and how to present beautifully the working of the client’s need and their advantages be highlighted.</p>
  </article>

  <div class="col-sep" style="left:396px"></div>

  <h2 class="col-title" style="left:421px;font-weight:400">Our Partners</h2>
  <div class="col-rule" style="left:421px;width:343px"></div>
  <div class="partner" style="left:420px;top:656px">Corvanta</div>
  <div class="partner" style="left:594px;top:656px">Halverin</div>
  <div class="partner" style="left:420px;top:751px">Trevik</div>
  <div class="partner" style="left:600px;top:751px">Olsaro</div>

  <div class="col-sep" style="left:783px"></div>

  <h2 class="col-title" style="left:804px;font-weight:400">Our Clients &amp; Customers</h2>
  <div class="col-rule" style="left:804px;width:346px"></div>
  <div class="client" style="left:806px;top:626px">Fennly</div>
  <div class="client" style="left:929px;top:626px">Lumaro</div>
  <div class="client" style="left:1050px;top:626px">Vestrel</div>
  <div class="client" style="left:806px;top:725px">Qandor</div>
  <div class="client" style="left:929px;top:725px">Ribelle</div>
  <div class="client" style="left:1050px;top:725px">Tamsin</div>
</section>

<footer class="site-footer">
  <div class="footer-nav">Home<span>|</span>About Company<span>|</span>Services<span>|</span>Download<span>|</span>Support<span>|</span>Products<span>|</span>Resources<span>|</span>News<span>|</span>Log In<span>|</span>Contact<span>|</span>Policy<span>|</span>Developers<span>|</span>About Us<span>|</span>Contact Us</div>
  <div class="copyright">Copyright © 2012 Company Name<span style="margin:0 7px">|</span>Term &amp; Conditions</div>
</footer>

</body>
</html>
```